Brochure Design Project

PLEASE USE THE ATTACHED WORD DOC ONLY AS A GUIDE- I WANT TO SEE A TRUE DESIGN AND NOT JUST A RECREATE OF MY CONTENT.

We need a brochure that is geared towards a service mentality. less tech/bold and something very approachable.

we will look for a design concept and then finalize the content laters.

Target Market(s)

nurses and business owners

Industry/Entity Type

Tech

```html
<!DOCTYPE html>
<html lang="en">
<head>
<meta charset="utf-8">
<title>Customized Health Care Brochure Panel</title>
<link rel="stylesheet" href="https://fonts.googleapis.com/css2?family=Dancing+Script:wght@700&family=Source+Sans+3:ital,wght@0,400;0,600;1,400&display=swap">
<style>
  :root {
    --blue-deep: #1877c0;
    --blue-bright: #00b4e8;
    --blue-title: #1b8fd0;
    --purple: #8c3a8e;
    --purple-light: #c996c9;
    --ink: #2b2b2b;
    --ink-soft: #4a4a4a;
    --panel: #eef4f8;
    --white: #ffffff;
  }
  * { margin: 0; padding: 0; box-sizing: border-box; }
  html, body { width: 1200px; height: 927px; overflow: hidden; background: var(--white); }
  .brochure {
    position: relative;
    width: 1200px;
    height: 927px;
    overflow: hidden;
    font-family: "Source Sans 3", "Myriad Pro", Arial, sans-serif;
    color: var(--ink);
  }
  .hero-band, .footer-band { position: absolute; left: 0; }
  .hero-band { top: 0; width: 1200px; height: 370px; }
  .footer-band { bottom: 0; width: 1200px; height: 50px; }

  .hero-title {
    position: absolute; left: 33px; top: 56px;
    font-family: "Dancing Script", cursive;
    font-size: 33px; line-height: 40px;
    color: var(--white);
  }
  .hero-lede {
    position: absolute; left: 31px; top: 152px; width: 345px;
    font-size: 22px; line-height: 36px;
    color: var(--white);
  }
  .hero-photo {
    position: absolute; left: 430px; top: 60px;
    width: 340px; height: 226px;
    background: linear-gradient(135deg, #f4f6f8 0%, #dfe6ec 55%, #c9d3dc 100%);
  }

  .extras-panel {
    position: absolute; left: 831px; top: 60px;
    width: 338px; height: 373px;
    background: var(--panel);
    box-shadow: 0 2px 6px rgba(0,0,0,0.25);
    padding: 14px 14px 0 14px;
  }
  .extras-title {
    font-size: 31px; font-weight: 600; color: var(--blue-title);
    line-height: 36px; margin-bottom: 6px;
  }
  .extras-list { list-style: none; }
  .extras-list li {
    position: relative; padding-left: 12px;
    font-style: italic; font-size: 18.5px; line-height: 27.5px;
    color: var(--ink-soft); margin-bottom: 5px;
  }
  .extras-list li::before {
    content: "•"; position: absolute; left: 0; top: 0;
    color: var(--blue-title); font-style: normal; font-size: 15px;
  }

  .feature {
    position: absolute; width: 340px;
    font-size: 17px; line-height: 23.4px; color: var(--ink);
  }
  .feature-name {
    font-family: "Dancing Script", cursive;
    font-size: 28px; line-height: 23px;
    color: var(--purple);
  }
  .col-left { left: 31px; }
  .col-mid { left: 431px; width: 336px; }
  .col-right { left: 831px; }
</style>
</head>
<body>
<main class="brochure">
  <svg class="hero-band" viewBox="0 0 1200 370" aria-hidden="true">
    <defs>
      <linearGradient id="heroFill" x1="0" y1="0" x2="1" y2="0">
        <stop offset="0" stop-color="#1a7cc4"/>
        <stop offset="0.45" stop-color="#00b4e8"/>
        <stop offset="0.75" stop-color="#12a3dd"/>
        <stop offset="1" stop-color="#1a80c6"/>
      </linearGradient>
    </defs>
    <path d="M0 0 H1200 V335 C1040 350 900 330 760 318 C600 305 430 310 260 318 C150 323 70 330 0 338 Z" fill="url(#heroFill)"/>
    <path d="M0 338 C70 330 150 323 260 318 C430 310 600 305 760 318 C900 330 1040 350 1200 335 V346 C1040 360 900 342 760 330 C600 318 430 322 260 330 C150 335 70 342 0 350 Z" fill="#bfe6f6"/>
  </svg>

  <h1 class="hero-title">We are experts in<br>Customized health care</h1>
  <p class="hero-lede">By compounding medications, we can improve patient out&shy;comes and simplify medication administration caregivers.</p>

  <div class="hero-photo" role="img" aria-label="Photo of a pharmacist showing a medication bottle to a smiling senior couple at a desk"></div>

  <aside class="extras-panel">
    <h2 class="extras-title">We also provide:</h2>
    <ul class="extras-list">
      <li>Customized Combinations simplify medication admistration</li>
      <li>Dosage form Changes</li>
      <li>Transdermal Pain Management for site specific therapy</li>
      <li>Sugar-Free therapy for diabetic patients</li>
      <li>Lactose Capsules</li>
      <li>Customized dosage for kidney or liver failure patients</li>
    </ul>
  </aside>

  <section class="feature col-left" style="top:364px">
    <span class="feature-name">Service :</span> Our service sets us apart from retail pharmacies as well as large impersonal pharmacies. As your pharmacy partner, you’ll have access to our pharmacy owners knowledge staff to address concerns, find solutions, and ultimately provide better care while increasing your profitability.
  </section>
  <section class="feature col-left" style="top:594px">
    <span class="feature-name">Timely Deliveries</span> When it comes to timely deliveries, Harborview has multiple solutions to get you the medications you need quickly. With our pharmacy network, we can deliver medications at anytime, for any reason.
  </section>
  <section class="feature col-left" style="top:774px">
    <span class="feature-name">MAR or EMAR</span> We support EMAR or provide paper MARs if desired. Our goal is to work with your current system, not against it.
  </section>

  <section class="feature col-mid" style="top:364px">
    <span class="feature-name">Customized Formularies</span> We help you manage healthcare costs and limit staff dispensing time by creating formularies that focus on generic and customized compounded medications.
  </section>
  <section class="feature col-mid" style="top:520px">
    <span class="feature-name">Medicare Part D Partners</span><br>We handle therapeutic interchange, prior authorizations, and physician global authorizations so you don’t have to.
  </section>
  <section class="feature col-mid" style="top:659px">
    <span class="feature-name">Medicare Part A</span> Utilizing our pharmacy network, we minimize billing issues with price transparency and accuracy. This allows us focus on corporate strategies to manage your pharmacy expenses. Monthly reports helps identify trends, non-formulary utilization and clinical standards to ensure your facility is saving time and money.
  </section>

  <section class="feature col-right" style="top:479px">
    <span class="feature-name">Technology Solutions</span> Harborview provides great time saving technology solutions that you won’t find with other local retail pharmacies. We are constantly offer new and exciting ways to reduce staff time and increase profitability
  </section>
  <section class="feature col-right" style="top:664px">
    <span class="feature-name">Consultant Pharmacists</span> Our pharmacists provide regulatory compliance assistance to minimize your risk and reduce issues during facility surveys.
  </section>
  <section class="feature col-right" style="top:795px">
    <span class="feature-name">Continuing Education</span> CE for caretakers leads to better outcomes for your residents and your bottom line.
  </section>

  <svg class="footer-band" viewBox="0 0 1200 50" aria-hidden="true">
    <defs>
      <linearGradient id="footerFill" x1="0" y1="0" x2="1" y2="0">
        <stop offset="0" stop-color="#8c3a8e"/>
        <stop offset="0.5" stop-color="#c996c9"/>
        <stop offset="1" stop-color="#8c3a8e"/>
      </linearGradient>
    </defs>
    <path d="M0 20 C300 10 700 10 1200 22 V50 H0 Z" fill="url(#footerFill)"/>
    <path d="M0 20 C300 10 700 10 1200 22 V26 C700 15 300 15 0 25 Z" fill="#ffffff" opacity="0.6"/>
  </svg>
</main>
</body>
</html>
```